Kettlebrook Fixers Co. Business Card & Stationary
Roving Gadget Mend Service
Bright & Fun-filled
Dorian P. Hale
Service Director
P.O. Box 530697
Cedarholt, TX 75512
dphale@corvanmail.com
Expert Repair on All Major Brands & Models.
Mention this Special for $15 Off Any Job Requiring Parts!

```html
<!DOCTYPE html>
<html lang="en">
<head>
<meta charset="UTF-8">
<title>Kettlebrook Fixers Co. Business Card</title>
<link href="https://fonts.googleapis.com/css2?family=Arimo:wght@400;700&display=swap" rel="stylesheet">
<style>
  :root {
    --bg: #d9dadc;
    --card: #ffffff;
    --blue: #1aa3dc;
    --yellow: #f5e10e;
    --ink: #2a2a2a;
    --grey: #6b6b6b;
  }
  * { box-sizing: border-box; margin: 0; padding: 0; }
  html, body { width: 1200px; height: 838px; overflow: hidden; }
  body {
    background: var(--bg);
    font-family: "Arimo", Arial, sans-serif;
    position: relative;
  }
  .card {
    position: absolute;
    width: 640px;
    height: 366px;
    left: 280px;
    background: var(--card);
    box-shadow: 0 6px 20px rgba(0,0,0,0.18);
    overflow: hidden;
  }
  .card-back { top: 22px; }
  .card-front { top: 450px; }
  .card-decor { position: absolute; inset: 0; }
  .brand {
    position: absolute;
    display: flex;
    align-items: center;
    gap: 10px;
    color: var(--blue);
    font-weight: 700;
    font-size: 24px;
    line-height: 1.1;
  }
  .brand-dot {
    width: 22px; height: 22px; border-radius: 50%;
    background: var(--blue); flex: none;
  }
  .card-back .brand { left: 50%; top: 50%; transform: translate(-50%, -50%); font-size: 30px; }
  .card-front .brand { left: 130px; top: 62px; width: 260px; }
  .offer {
    position: absolute; left: 70px; top: 200px; width: 250px;
    font-size: 11px; line-height: 1.45; color: var(--grey);
  }
  .contact { position: absolute; left: 380px; top: 172px; color: var(--ink); }
  .contact-name { font-size: 24px; color: var(--blue); font-weight: 400; }
  .contact-title { font-size: 11px; color: var(--grey); margin-bottom: 16px; }
  .contact-line { font-size: 12px; line-height: 1.5; display: flex; align-items: center; gap: 6px; }
  .contact-gap { margin-bottom: 10px; }
  .icon { width: 12px; height: 12px; flex: none; }
</style>
</head>
<body>
  <section class="card card-back">
    <div class="brand"><span class="brand-dot"></span>Roving Gadget Mend Service</div>
  </section>

  <section class="card card-front">
    <svg class="card-decor" viewBox="0 0 640 366" aria-hidden="true">
      <polygon points="0,0 70,0 0,100" fill="var(--yellow)"/>
      <path d="M0,120 Q25,250 140,366 L120,366 Q15,260 0,150 Z" fill="var(--ink)"/>
      <path d="M0,170 Q15,280 95,366 L0,366 Z" fill="var(--blue)"/>
      <path d="M330,366 Q480,340 640,300 L640,366 Z" fill="var(--blue)"/>
    </svg>
    <div class="brand"><span class="brand-dot"></span>Roving Gadget Mend Service</div>
    <p class="offer">Expert Repair on All Major Brands &amp; Models.<br>Mention this Special for $15 Off Any Job Requiring Parts!</p>
    <div class="contact">
      <h1 class="contact-name">Dorian P. Hale</h1>
      <p class="contact-title">Service Director</p>
      <p class="contact-line">P.O. Box 530697</p>
      <p class="contact-line contact-gap">Cedarholt, TX 75512</p>
      <p class="contact-line">
        <svg class="icon" viewBox="0 0 12 12"><path d="M2 1 L4.5 1 L5.5 3.5 L4 4.5 Q5 7 7.5 8 L8.5 6.5 L11 7.5 L11 10 Q6 11 2 6 Q1 3 2 1 Z" fill="var(--yellow)"/></svg>
        (281) 555-0148
      </p>
      <p class="contact-line">
        <svg class="icon" viewBox="0 0 12 12"><rect x="1" y="2.5" width="10" height="7" fill="var(--yellow)"/><path d="M1 2.5 L6 6.5 L11 2.5" stroke="#fff" fill="none"/></svg>
        dphale@corvanmail.com
      </p>
    </div>
  </section>
</body>
</html>
```